Visitenkarten-Design für ein Juwelier Geschäft
Zielgruppe
Juwelier Geschäft in modernem offenen design.
Zielgruppe sind kunden und partner/marken
Aufgabenstellung
schlichtes edles Design.
karten sollen später geprägt werden und einen goldschnitt erhalten

```html
<!DOCTYPE html>
<html lang="de">
<head>
<meta charset="utf-8">
<title>Visitenkarte – Roswald Juwelen</title>
<link rel="stylesheet" href="https://fonts.googleapis.com/css2?family=Montserrat:wght@300;400;500;700&display=swap">
<style>
  :root {
    --page-bg: #f3f3f3;
    --card-bg: #161616;
    --gold: #d4a12a;
    --white: #ffffff;
    --text-light: #e6e6e6;
  }
  html, body {
    margin: 0;
    padding: 0;
    width: 1200px;
    height: 1200px;
    overflow: hidden;
    background: var(--page-bg);
    font-family: "Montserrat", Arial, sans-serif;
  }
  .canvas {
    position: relative;
    width: 1200px;
    height: 1200px;
  }
  .card {
    position: absolute;
    left: 325px;
    width: 550px;
    height: 314px;
    background: var(--card-bg);
  }
  .card--front { top: 244px; }
  .card--back  { top: 642px; }
  .card__frame {
    position: absolute;
    left: 31px;
    top: 31px;
    width: 483px;
    height: 247px;
    border: 2.5px solid var(--gold);
  }
  .brand-name {
    position: absolute;
    left: 0;
    width: 100%;
    top: 112px;
    text-align: center;
    color: var(--white);
    font-weight: 700;
    font-size: 44px;
    letter-spacing: 4px;
    line-height: 1;
  }
  .front-url {
    position: absolute;
    left: 0;
    width: 100%;
    top: 203px;
    text-align: center;
    color: var(--white);
    font-weight: 300;
    font-size: 17px;
    letter-spacing: 0.3px;
  }
  .person-name {
    position: absolute;
    left: 79px;
    top: 69px;
    color: var(--white);
    font-weight: 500;
    font-size: 24px;
    letter-spacing: 0.3px;
  }
  .person-role {
    position: absolute;
    left: 79px;
    top: 98px;
    color: var(--gold);
    font-weight: 400;
    font-size: 18px;
    letter-spacing: 1.2px;
  }
  .address, .contact {
    position: absolute;
    top: 176px;
    margin: 0;
    padding: 0;
    list-style: none;
    color: var(--text-light);
    font-weight: 300;
    font-size: 13px;
  }
  .address { left: 79px; }
  .contact { left: 334px; }
  .address li, .contact li {
    height: 24px;
    line-height: 24px;
    display: flex;
    align-items: center;
  }
  .contact__icon {
    width: 12px;
    height: 12px;
    margin-right: 9px;
    flex: none;
  }
</style>
</head>
<body>
<main class="canvas">

  <section class="card card--front" aria-label="Vorderseite">
    <div class="card__frame"></div>
    <div class="brand-name">ROSWALD</div>
    <div class="front-url">www.roswald.de</div>
  </section>

  <section class="card card--back" aria-label="Rückseite">
    <div class="card__frame"></div>
    <div class="person-name">Bernhard</div>
    <div class="person-role">Manager</div>

    <ul class="address">
      <li>Niederlassung Lindholm</li>
      <li>Mühlenweg 14</li>
      <li>25421 Lindholm</li>
    </ul>

    <ul class="contact">
      <li>
        <svg class="contact__icon" viewBox="0 0 12 12" fill="none" stroke="#e6e6e6" stroke-width="1">
          <path d="M2.5 1 L4.5 3.5 L3.5 4.8 Q5 7.3 7.2 8.5 L8.5 7.5 L11 9.5 L9.8 11 Q5 10.5 1 3 Z"/>
        </svg>
        +49 04561-27084
      </li>
      <li>
        <svg class="contact__icon" viewBox="0 0 12 12" fill="none" stroke="#e6e6e6" stroke-width="1">
          <rect x="0.8" y="2.3" width="10.4" height="7.4"/>
          <path d="M0.8 2.3 L6 6.5 L11.2 2.3"/>
        </svg>
        info@roswald.de
      </li>
      <li>
        <svg class="contact__icon" viewBox="0 0 12 12" fill="none" stroke="#e6e6e6" stroke-width="1">
          <circle cx="6" cy="6" r="5"/>
          <ellipse cx="6" cy="6" rx="2.2" ry="5"/>
          <path d="M1 6 H11 M1.8 3.5 H10.2 M1.8 8.5 H10.2"/>
        </svg>
        www.roswald.de
      </li>
    </ul>
  </section>

</main>
</body>
</html>
```